Personal Training

The name of my company is Heron Fitness. I am looking for a design that will feature the 8 components I am utilizing in my workouts (strength, flexibility, agility, core, power, balance, cardiovacular, speed) and represent the spider. It is not essesstial to have a spider for my logo but would be nice. If a spider is used please do not use a logo like Gullwoman, a tarantula, or anything scary involving a spider (I have female clients who would get scared) lol
If you need me to provide more information please let me know. Feel free to check my website for ideas but ignore the pictures on my site as those are not pictures of me or clients
Thank you in advance!

Industry/Entity Type

Fitness

Contact Information for Business Card

Mark Delaney
Company Name: Heron Fitness
Tag line: 8 elements for a stronger you
Website: hernfit4.example
Email: mark@hernfit4.example
Cell: 555-314-2086

CQBL Certified Personal Trainer
CPR AED National Pulse Federation
B.A. Exercise Physiology W.K.R., 2004

```html
<!DOCTYPE html>
<html lang="en">
<head>
<meta charset="utf-8">
<title>Heron Fitness – Business Card</title>
<link href="https://fonts.googleapis.com/css2?family=Arimo:wght@400;700&display=swap" rel="stylesheet">
<style>
  :root {
    --backdrop: #2a2a2a;
    --card-black: #1c1c1c;
    --brand-red: #d13b36;
    --brand-red-dark: #a92a27;
    --ink: #1e1e1e;
    --paper: #f2f2f2;
    --light-grey: #d8d8d8;
    --credential: #f4c2bd;
    --label: #f6dcda;
  }
  * { margin: 0; padding: 0; box-sizing: border-box; }
  html, body {
    width: 1200px; height: 900px; overflow: hidden;
    background: var(--backdrop);
    font-family: "Arimo", Arial, sans-serif;
  }
  .card {
    position: absolute;
    width: 560px; height: 320px;
    border-radius: 4px;
    overflow: hidden;
    box-shadow: 0 10px 30px rgba(0,0,0,.5);
  }

  /* Back side */
  .card-back {
    left: 140px; top: 90px;
    background: var(--card-black);
  }
  .card-back .brand {
    position: absolute; left: 250px; top: 128px;
    display: flex; align-items: center; gap: 12px;
  }
  .card-back .brand-dot {
    width: 52px; height: 52px; border-radius: 50%;
    background: var(--brand-red);
    flex: none;
  }
  .card-back .brand-name {
    font-size: 28px; font-weight: 700; color: var(--light-grey);
    line-height: 1;
  }
  .card-back .tagline {
    font-size: 10px; font-weight: 700; color: var(--light-grey);
    letter-spacing: 1.2px; margin-top: 4px;
  }

  /* Front side */
  .card-front { left: 500px; top: 490px; }
  .card-front .wave-bg { position: absolute; inset: 0; }
  .card-front .brand {
    position: absolute; left: 16px; top: 36px;
    display: flex; align-items: center; gap: 14px;
  }
  .card-front .brand-dot {
    width: 60px; height: 60px; border-radius: 50%;
    background: #fff;
    flex: none;
  }
  .card-front .brand-name {
    font-size: 34px; font-weight: 700; color: #fff; line-height: 1;
  }
  .card-front .tagline {
    font-size: 12px; font-weight: 700; color: var(--ink);
    letter-spacing: 1.6px; margin-top: 3px;
  }
  .trainer { position: absolute; left: 30px; top: 146px; }
  .trainer-name {
    font-size: 27px; font-weight: 700; color: var(--ink);
    letter-spacing: .5px;
  }
  .credentials {
    list-style: none; margin-top: 4px;
    font-size: 13px; line-height: 16px; color: var(--credential);
  }
  .divider {
    position: absolute; left: 328px; top: 110px;
    width: 2px; height: 92px; background: #f3d8d6;
  }
  .contact {
    position: absolute; left: 340px; top: 118px;
    display: grid; grid-template-columns: auto auto; column-gap: 6px;
    font-size: 13px; font-weight: 700; line-height: 18px;
  }
  .contact dt { color: var(--label); letter-spacing: .5px; }
  .contact dd { color: var(--ink); }
  .site-url {
    position: absolute; left: 48px; top: 278px;
    font-size: 17px; font-weight: 700; color: var(--ink);
    letter-spacing: .8px;
  }
</style>
</head>
<body>

<section class="card card-back" aria-label="Business card back">
  <div class="brand">
    <span class="brand-dot"></span>
    <div>
      <div class="brand-name">Heron Fitness</div>
      <div class="tagline">8 elements for a stronger you</div>
    </div>
  </div>
</section>

<section class="card card-front" aria-label="Business card front">
  <svg class="wave-bg" width="560" height="320" viewBox="0 0 560 320" aria-hidden="true">
    <defs>
      <linearGradient id="redFill" x1="0" y1="0" x2="1" y2="1">
        <stop offset="0" stop-color="var(--brand-red)"/>
        <stop offset="1" stop-color="var(--brand-red-dark)"/>
      </linearGradient>
    </defs>
    <rect width="560" height="320" fill="url(#redFill)"/>
    <path d="M0,320 L0,262 C140,222 290,262 420,212 C480,188 530,176 560,172 L560,320 Z" fill="var(--paper)"/>
    <path d="M0,262 C140,222 290,262 420,212 C480,188 530,176 560,172" fill="none" stroke="var(--ink)" stroke-width="4"/>
  </svg>

  <div class="brand">
    <span class="brand-dot"></span>
    <div>
      <div class="brand-name">Heron Fitness</div>
      <div class="tagline">8 elements for a stronger you</div>
    </div>
  </div>

  <div class="trainer">
    <h1 class="trainer-name">Mark Delaney</h1>
    <ul class="credentials">
      <li>CQBL Certified Personal Trainer</li>
      <li>CPR AED National Pulse Federation</li>
      <li>B.A. Exercise Physiology W.K.R., 2004</li>
    </ul>
  </div>

  <span class="divider"></span>

  <dl class="contact">
    <dt>Cell :</dt><dd>555-314-2086</dd>
    <dt>Email:</dt><dd>mark@hernfit4.example</dd>
    <dt>Web :</dt><dd>www.hernfit4.example</dd>
  </dl>

  <div class="site-url">www.hernfit4.example</div>
</section>

</body>
</html>
```